Bright Leaf Company Needs New Packaging Design

We need a design to print directly on our stand up zip pouches, 6x9x3 in., to replace the labels we were applying on generic matte black pouches.

We'd like to keep the current color theme of matte black + [Flavor Color] (in this case, fushia) to communicate the idea of modern, luxury brand (please see velmora coffee brand) and stay somewhat close to the current label so our product will be recognized by actual customers. Other flavors will be a declination of the same layout, matte black + [flavor color]. Colors used should be vibrant, eye catching, to stand out from competition.

We also want to display the actual tea blend picture on the packaging so the consumer can see how beautiful the tea is. The font size for Quince Marigold Verbena should be big enough so it's readable when the product is seen in thumbnail format.

The front should have a seal/stamp close to a top corner with a big "100% Freshness Guarantee",

The company logo "The Brew Works" should be present on the front in a prominent spot. It's provided in the zip file from old label.

We need to display the net weight (4oz / 113g) and number of servings (makes 60 cups). Please refer to old label.

On the back side we need a space for the UPC barcode at the bottom, the company address, a space for the brand's story/mission, steeping instructions with icons (see current label), ingredients and another section featuring our other products. All fonts should be 10pt or bigger.

Artwork of the current label current label is available here
https://files.example-share.net/folders/7Qx2mR9pLk4vNw8sTz3yHc6bJd?key=1-P58rbnVtLKS2wXhyQfme&mode=view

Target Market(s)

USA market, Women ages 25-45, young & young at heart, trendy, health conscious, luxury

Industry/Entity Type

Premium Loose Leaf Tea

Font styles to use
Other font styles liked:
• fonts provided in zip file

Colors
E54698
E96AAD
F1A4CE
F9D9EA
FCEFF6

Requirements
Must have
• See description
Should not have
• Asian look and feel

```html
<!DOCTYPE html>
<html lang="en">
<head>
<meta charset="utf-8">
<title>The Brew Works – Quince Marigold Verbena Pouch</title>
<link href="https://fonts.googleapis.com/css2?family=Londrina+Solid:wght@400;900&family=Sacramento&family=Poppins:wght@400;500&display=swap" rel="stylesheet">
<style>
  :root {
    --backdrop: #e62a52;
    --pouch-black: #121212;
    --pouch-black-soft: #1e1e1e;
    --pouch-edge: #050505;
    --ink-white: #ffffff;
    --flavor: #e8305a;
    --flavor-deep: #d51f4b;
    --gold: #d9a441;
    --seal-grey: #cfd3d2;
    --tea-orange: #e07a26;
    --tea-red: #b0262a;
    --tea-amber: #c8932c;
    --bowl-white: #f4f2ef;
  }
  * { box-sizing: border-box; margin: 0; padding: 0; }
  html, body {
    width: 1200px; height: 840px; overflow: hidden;
    background: var(--backdrop);
  }
  .stage { position: relative; width: 1200px; height: 840px; }

  .pouch {
    position: absolute; left: 380px; top: 70px;
    width: 440px; height: 700px;
    border-radius: 6px;
    background: linear-gradient(100deg, var(--pouch-black-soft) 0%, var(--pouch-black) 45%, #1a1a1a 70%, var(--pouch-edge) 100%);
    overflow: hidden;
    font-family: "Londrina Solid", sans-serif;
    color: var(--ink-white);
  }
  .pouch-texture {
    position: absolute; inset: 0;
    background: linear-gradient(180deg, rgba(255,255,255,0.05) 0%, rgba(255,255,255,0) 30%, rgba(255,255,255,0.03) 60%, rgba(0,0,0,0.15) 100%);
  }
  .zip-seal {
    position: absolute; left: 0; right: 0; top: 66px; height: 3px;
    background: rgba(255,255,255,0.12);
  }

  .brand {
    position: absolute; left: 54px; top: 118px;
    font-family: "Londrina Solid", sans-serif; font-weight: 400;
    color: var(--ink-white); line-height: 1;
  }
  .brand-small { display: block; font-size: 30px; margin-left: 6px; }
  .brand-large { display: block; font-size: 70px; }
  .brand-mark {
    position: absolute; left: 100px; top: 0; width: 22px; height: 22px;
    border-radius: 50%; background: var(--flavor);
  }

  .organic-seal {
    position: absolute; left: 379px; top: 177px;
    width: 42px; height: 42px; border-radius: 50%;
    background: var(--seal-grey); border: 3px solid var(--ink-white);
  }

  .blend-photo {
    position: absolute; left: 192px; top: 272px;
    width: 238px; height: 238px; border-radius: 50%;
    background: radial-gradient(circle at 50% 50%, var(--tea-orange) 0%, var(--tea-red) 35%, var(--tea-amber) 68%, var(--bowl-white) 72%, var(--bowl-white) 100%);
  }

  .flavor-name {
    position: absolute; left: 36px; top: 276px;
    text-transform: uppercase; line-height: 0.95; font-weight: 400;
  }
  .flavor-name span { display: block; }
  .flavor-big { font-size: 44px; }
  .flavor-mid { font-size: 30px; margin-left: 12px; }

  .ribbons { position: absolute; left: 30px; top: 400px; }
  .ribbon {
    display: block; width: fit-content;
    background: var(--flavor); color: var(--ink-white);
    font-size: 18px; text-transform: uppercase; letter-spacing: 0.3px;
    padding: 1px 10px 2px;
    transform: rotate(-2deg);
  }
  .ribbon + .ribbon { margin-top: 2px; margin-left: -4px; }

  .caffeine-free {
    position: absolute; left: 86px; top: 452px;
    font-family: "Sacramento", cursive; font-size: 48px; line-height: 0.8;
    transform: rotate(-6deg);
  }
  .caffeine-free span { display: block; }
  .caffeine-free span + span { margin-left: 46px; }

  .steeping {
    position: absolute; left: 12px; top: 516px;
    display: flex; gap: 14px;
    font-family: "Poppins", sans-serif; font-size: 8.5px; line-height: 1.25;
    color: var(--gold); text-align: center;
  }
  .steep-step { width: 82px; display: flex; flex-direction: column; align-items: center; }
  .steep-step svg { width: 26px; height: 26px; margin-bottom: 4px; }

  .cups-stamp {
    position: absolute; left: 332px; top: 536px;
    width: 60px; height: 60px; border-radius: 50%;
    border: 3px solid var(--flavor-deep);
    color: var(--flavor-deep); background: rgba(255,255,255,0.9);
    display: flex; flex-direction: column; align-items: center; justify-content: center;
    font-weight: 900; line-height: 0.9; transform: rotate(-18deg);
  }
  .cups-number { font-size: 22px; }
  .cups-label { font-size: 12px; }

  .net-weight {
    position: absolute; left: 0; right: 0; top: 590px;
    text-align: center; font-size: 22px; letter-spacing: 1px;
    text-transform: uppercase;
  }
</style>
</head>
<body>
<main class="stage">
  <section class="pouch" aria-label="Front of tea pouch">
    <div class="pouch-texture" role="img" aria-label="Dark black wood grain texture"></div>
    <div class="zip-seal"></div>

    <div class="brand">
      <span class="brand-mark"></span>
      <span class="brand-small">The</span>
      <span class="brand-large">Brew</span>
      <span class="brand-small">Works</span>
    </div>

    <div class="organic-seal" aria-label="Organic certification seal"></div>

    <div class="blend-photo" role="img" aria-label="White bowl filled with loose quince, marigold and verbena herbal tea blend"></div>

    <h1 class="flavor-name">
      <span class="flavor-big">Quince</span>
      <span class="flavor-mid">Marigold</span>
      <span class="flavor-big">Verbena</span>
    </h1>

    <div class="ribbons">
      <span class="ribbon">Calming &amp; Soothing</span>
      <span class="ribbon">Premium Loose Herbal Tea</span>
    </div>

    <p class="caffeine-free"><span>Caffeine</span><span>Free</span></p>

    <ul class="steeping">
      <li class="steep-step">
        <svg viewBox="0 0 26 26" fill="none" stroke="currentColor" stroke-width="1.6" stroke-linecap="round">
          <ellipse cx="8" cy="8" rx="5" ry="3.5" transform="rotate(-40 8 8)"/>
          <line x1="11" y1="11" x2="22" y2="22"/>
        </svg>
        Qty Per Cup<br>1-2 Heaping<br>Teaspoons
      </li>
      <li class="steep-step">
        <svg viewBox="0 0 26 26" fill="none" stroke="currentColor" stroke-width="1.6" stroke-linecap="round">
          <path d="M11 4 v12 a4 4 0 1 0 4 0 V4 a2 2 0 0 0 -4 0z"/>
          <line x1="13" y1="9" x2="13" y2="18"/>
          <line x1="18" y1="6" x2="21" y2="6"/><line x1="18" y1="10" x2="21" y2="10"/>
        </svg>
        Temperature<br>206° F / 95° C
      </li>
      <li class="steep-step">
        <svg viewBox="0 0 26 26" fill="none" stroke="currentColor" stroke-width="1.6" stroke-linecap="round">
          <circle cx="13" cy="14" r="8"/>
          <line x1="13" y1="14" x2="13" y2="9"/><line x1="13" y1="14" x2="16" y2="16"/>
          <line x1="10" y1="3" x2="16" y2="3"/>
        </svg>
        Steeping Time<br>5-7 Mins
      </li>
    </ul>

    <div class="cups-stamp">
      <span class="cups-number">60</span>
      <span class="cups-label">CUPS</span>
    </div>

    <p class="net-weight">Net Weight (4oz / 113g)</p>
  </section>
</main>
</body>
</html>
```